Corbel Family Farm fresh honey jar label

I need a label for jars of honey harvested at our farm. These are for gifts and personal use. We are looking to incorporate our farm brand into the label. We would like the design to take the existing brand and add some element like bees, honey, flowers, or hives to indicate the contents. We want the design to feel homemade and authentic without feeling cheap or hoaky

Requirements
Must have
• The label must be made to fit a 1" x2" rectangular label. The label must include the attached family brand. The label must include the text "Corbel Family Farms" "Pinebrook, USA" "Farm Fresh Honey". The label will be printed on off-white paper
Nice to have
• It would be nice to have illustrations of bees or flowers around the logo or hives or honeycombs. The label should have a vintage feel
Should not have
• The label should not feel overly cartoonish or hoaky

```html
<!DOCTYPE html>
<html lang="en">
<head>
<meta charset="utf-8">
<title>Corbel Family Farm – Farm Fresh Honey Label</title>
<link href="https://fonts.googleapis.com/css2?family=Cormorant+SC:wght@500;700&display=swap" rel="stylesheet">
<style>
  :root {
    --canvas: #fbfbfa;
    --paper: #f1f0ec;
    --ink: #4a4542;
    --band: #6b6561;
    --band-light: #f4f2ee;
    --badge: #e9e3d6;
    --flower-warm: #f2b45a;
    --flower-cream: #f5ead2;
    --flower-rose: #e8607a;
    --flower-leaf: #9fb49a;
  }
  * { box-sizing: border-box; margin: 0; padding: 0; }
  html, body {
    width: 1200px; height: 1200px; overflow: hidden;
    background: var(--canvas);
  }
  body {
    display: flex; align-items: center; justify-content: center;
    font-family: "Cormorant SC", Georgia, serif;
    color: var(--ink);
  }
  .label {
    position: relative;
    width: 1000px; height: 655px;
    background: var(--paper);
    border-radius: 10px;
    overflow: hidden;
    box-shadow: 0 2px 10px rgba(0,0,0,0.08);
  }
  .brand-badge {
    position: absolute; left: 424px; top: 64px;
    width: 152px; height: 152px; border-radius: 50%;
    background: var(--badge);
    display: flex; flex-direction: column; align-items: center; justify-content: center;
    text-align: center;
    font-weight: 500; font-size: 17px; line-height: 1.15; letter-spacing: 0.06em;
    color: var(--ink);
  }
  .brand-badge .place { margin-top: 8px; font-size: 13px; }
  .floral {
    position: absolute; border-radius: 45% 50% 40% 55%;
  }
  .floral-left {
    left: 36px; top: 190px; width: 295px; height: 300px;
    background: radial-gradient(circle at 45% 45%, var(--flower-warm) 0%, #f6cf8e 35%, var(--flower-cream) 65%, rgba(241,240,236,0) 80%);
  }
  .floral-right {
    left: 625px; top: 150px; width: 305px; height: 320px;
    background: radial-gradient(circle at 50% 50%, var(--flower-rose) 0%, #f0a0a6 32%, #f3dcc0 58%, rgba(241,240,236,0) 78%);
  }
  .title {
    position: absolute; left: 0; right: 0; top: 232px;
    text-align: center;
    font-weight: 700; font-size: 46px; line-height: 46px; letter-spacing: 0.04em;
  }
  .tagline {
    position: absolute; left: 0; right: 0; top: 488px;
    text-align: center;
    font-weight: 700; font-size: 19px; line-height: 23px; letter-spacing: 0.06em;
  }
  .footer-band {
    position: absolute; left: 0; bottom: 0; width: 1000px; height: 95px;
  }
  .footer-text {
    position: absolute; left: 0; right: 0; bottom: 28px;
    text-align: center; color: var(--band-light);
    font-weight: 700; font-size: 16px; letter-spacing: 0.14em;
  }
</style>
</head>
<body>
  <main class="label">
    <div class="brand-badge">
      <span class="name">Corbel<br>Family Farms</span>
      <span class="place">Pinebrook, USA</span>
    </div>

    <div class="floral floral-left" role="img" aria-label="Watercolour bouquet of golden poppies and white daisies with a bee"></div>
    <div class="floral floral-right" role="img" aria-label="Watercolour bouquet of pink dahlias, lavender and wildflowers with bees"></div>

    <h1 class="title">Farm<br>Fresh<br>Honey</h1>

    <p class="tagline">Raw Honey,<br>Harvested from our Bee Garden</p>

    <svg class="footer-band" viewBox="0 0 1000 95" preserveAspectRatio="none" aria-hidden="true">
      <path fill="var(--band)" d="M0 14 L40 12 L70 15 L110 11 L150 14 L190 10 L230 14 L270 12 L310 15 L350 11 L400 14 L440 12 L480 15 L520 10 L560 14 L600 12 L640 15 L680 11 L720 14 L760 12 L800 15 L840 11 L880 14 L920 12 L960 15 L1000 12 L1000 95 L0 95 Z"/>
    </svg>
    <p class="footer-text">Organically Cultivated Raw Honey</p>
  </main>
</body>
</html>
```